Black Car Limousine transportation business in Naples Florida

Brightway stand for my reliability and DPR stands for Devotion, P and R are the first initials of my children's names. It should show professionalism and a dedication to customer service. We keep our clients identities private. Show our professionalism. We are Black car Black tie company. We service transportation on a reserve basis to and from residents, airports, casinos, hotels,

Target Market(s)

It is a Private car service. High end clients. Businesses, Celebrity and athletes. Service to airports, hotels, special events.

Industry/Entity Type

Business

Contact Information for Business Card

A pearl metallic or Luster card. Standard business card size. Would like the name, Company email, show we take credit cards and phone number. Currently I don't have a website but will like to add later.

Logo Text

BRIGHTWAY DPR TRANSPORTATION

Font styles to use
Serif

Colors
eaeaea
000000

Requirements
Must have
• Must have Company email, show we take credit cards and phone number. Currently I don't have a website but will like to add later.
Nice to have
• Would like to stay with a black and white theme. Open to some color trim.
Should not have
• Open to suggestions

```html
<!DOCTYPE html>
<html lang="en">
<head>
<meta charset="utf-8">
<title>Brightway DPR Transportation – Business Card</title>
<link href="https://fonts.googleapis.com/css2?family=Lora:wght@400;600;700&display=swap" rel="stylesheet">
<style>
  :root {
    --backdrop: #4a4289;
    --card-front: #2a2f38;
    --card-front-light: #3a404b;
    --card-back: #3c3e43;
    --card-back-light: #4a4c51;
    --accent: #d9454a;
    --text-light: #ffffff;
    --text-muted: #d6d6d8;
  }
  * { box-sizing: border-box; margin: 0; padding: 0; }
  html, body { width: 1200px; height: 1200px; overflow: hidden; }
  body {
    background: var(--backdrop);
    font-family: "Lora", serif;
    position: relative;
  }
  .card {
    position: absolute;
    left: 180px;
    width: 840px;
    height: 480px;
    overflow: hidden;
    box-shadow: 0 18px 40px rgba(0,0,0,0.35);
  }
  .card--front { top: 90px; }
  .card--back { top: 630px; }
  .card__photo { position: absolute; inset: 0; }
  .card--front .card__photo {
    background: linear-gradient(120deg, var(--card-front) 0%, var(--card-front-light) 55%, var(--card-front) 100%);
  }
  .card--back .card__photo {
    background: linear-gradient(120deg, var(--card-back) 0%, var(--card-back-light) 50%, var(--card-back) 100%);
  }

  /* Front */
  .brand {
    position: absolute;
    left: 50%; top: 50%;
    transform: translate(-50%, -50%);
    display: flex; align-items: center; gap: 26px;
  }
  .brand__mark {
    width: 64px; height: 64px;
    background: var(--accent);
    flex: none;
  }
  .brand__name {
    color: var(--text-light);
    font-weight: 700;
    font-size: 44px;
    line-height: 1.15;
    letter-spacing: 0.5px;
    white-space: nowrap;
  }

  /* Back */
  .identity {
    position: absolute;
    top: 52px; left: 0; right: 0;
    display: flex; flex-direction: column; align-items: center;
    color: var(--text-light);
  }
  .identity__logo {
    display: flex; align-items: center; gap: 12px;
    margin-bottom: 26px;
  }
  .identity__logo-mark { width: 40px; height: 40px; background: var(--accent); }
  .identity__logo-name { font-weight: 700; font-size: 30px; letter-spacing: 1px; }
  .identity__name { font-weight: 600; font-size: 34px; letter-spacing: 1px; }
  .identity__role {
    color: var(--accent);
    font-weight: 600; font-size: 17px;
    letter-spacing: 6px; margin-top: 2px;
  }
  .contact {
    display: flex; align-items: center; gap: 14px;
    margin-top: 12px;
    font-size: 15px; color: var(--text-muted);
  }
  .contact__item { display: flex; align-items: center; gap: 7px; }
  .contact__icon { width: 14px; height: 14px; fill: var(--text-muted); }
  .details {
    position: absolute;
    bottom: 70px; left: 0; right: 0;
    display: flex; justify-content: center; gap: 26px;
  }
  .details__item {
    display: flex; align-items: center; gap: 9px;
    font-size: 15px; color: var(--text-muted);
    white-space: nowrap;
  }
  .details__dot {
    width: 28px; height: 28px; border-radius: 50%;
    background: var(--accent);
    display: flex; align-items: center; justify-content: center;
    flex: none;
  }
  .details__icon { width: 14px; height: 14px; fill: none; stroke: var(--text-light); stroke-width: 2; }
</style>
</head>
<body>

<section class="card card--front">
  <div class="card__photo" role="img" aria-label="Dark toned photograph of a chauffeured car interior with a passenger"></div>
  <div class="brand">
    <div class="brand__mark"></div>
    <div class="brand__name">Brightway DPR<br>Transportation</div>
  </div>
</section>

<section class="card card--back">
  <div class="card__photo" role="img" aria-label="Muted photograph of a passenger seated beside a car window"></div>
  <div class="identity">
    <div class="identity__logo">
      <div class="identity__logo-mark"></div>
      <span class="identity__logo-name">DPR</span>
    </div>
    <div class="identity__name">MARCUS HALE</div>
    <div class="identity__role">GENERAL MANAGER</div>
    <div class="contact">
      <span class="contact__item">
        <svg class="contact__icon" viewBox="0 0 24 24"><path d="M6.6 10.8a15.1 15.1 0 0 0 6.6 6.6l2.2-2.2a1 1 0 0 1 1-.25 11.4 11.4 0 0 0 3.6.57 1 1 0 0 1 1 1V20a1 1 0 0 1-1 1A17 17 0 0 1 3 4a1 1 0 0 1 1-1h3.5a1 1 0 0 1 1 1c0 1.25.2 2.45.57 3.57a1 1 0 0 1-.25 1z"/></svg>
        +1 239 555 0148
      </span>
      <span>|</span>
      <span class="contact__item">
        <svg class="contact__icon" viewBox="0 0 24 24"><path d="M2 5h20v14H2z"/><path d="M2 5l10 7 10-7" fill="none" stroke="#3c3e43" stroke-width="2"/></svg>
        ride@brightwaydpr.com
      </span>
    </div>
  </div>
  <div class="details">
    <span class="details__item">
      <span class="details__dot"><svg class="details__icon" viewBox="0 0 24 24"><rect x="2" y="5" width="20" height="14" rx="2"/><path d="M2 10h20"/></svg></span>
      Credit cards accepted
    </span>
    <span class="details__item">
      <span class="details__dot"><svg class="details__icon" viewBox="0 0 24 24"><circle cx="12" cy="12" r="9"/><path d="M12 7v5l3 2"/></svg></span>
      By reservation
    </span>
    <span class="details__item">
      <span class="details__dot"><svg class="details__icon" viewBox="0 0 24 24"><path d="M12 22s7-7 7-12a7 7 0 0 0-14 0c0 5 7 12 7 12z"/><circle cx="12" cy="10" r="2.5"/></svg></span>
      Naples, Florida
    </span>
    <span class="details__item">
      <span class="details__dot"><svg class="details__icon" viewBox="0 0 24 24"><circle cx="12" cy="12" r="9"/><path d="M3 12h18M12 3c3 3 3 15 0 18M12 3c-3 3-3 15 0 18"/></svg></span>
      Website coming soon
    </span>
  </div>
</section>

</body>
</html>
```